Aged Care Consultancy Business needs a business card design

I need a two sided business card - I want it clean and professional. Surprise me

Target Market(s)

middle aged and ageing victorians

Industry/Entity Type

Health Care

Contact Information for Business Card

Text to be included

Logo
Aged Care Consulting Services
Professional, Reliable, Affordable

Tovan Brelsick
Director
0427 31 64 92 (larger)
1300 73 29 41
tovan@wadolire.com.au
www.wadolcare.com.au
Facebook (details TBA)

include little icons beside the contact info:

- Envelope = email
- Phone = phone
- Globe = website

Font styles to use
Serif
Sans Serif

Requirements
Must have
• look proffesional and clean

```html
<!DOCTYPE html>
<html lang="en">
<head>
<meta charset="utf-8">
<title>Wadol Care – Business Card</title>
<link href="https://fonts.googleapis.com/css2?family=Red+Hat+Display:wght@400;700&family=Roboto:wght@400;500;700&family=Roboto+Condensed:wght@500&display=swap" rel="stylesheet">
<style>
  :root {
    --navy: #1d3f7c;
    --orange: #e89424;
    --ink: #3a3a3a;
    --icon: #8a8a8a;
    --paper: #ffffff;
    --backdrop: #e9e7e4;
  }
  * { margin: 0; padding: 0; box-sizing: border-box; }
  html, body { width: 1200px; height: 1178px; overflow: hidden; background: var(--backdrop); }
  .canvas { position: relative; width: 1200px; height: 1178px; }

  .card {
    position: absolute; left: 204px; width: 788px; height: 449px;
    background: var(--paper);
    box-shadow: 0 4px 14px rgba(0,0,0,0.18);
    overflow: hidden;
  }
  .card--front { top: 79px; }
  .card--back { top: 625px; }

  .accent-bar { position: absolute; background: var(--orange); }

  .brand-name {
    position: absolute; font-family: "Roboto", sans-serif; font-weight: 700;
    color: var(--navy); white-space: nowrap; letter-spacing: 0.5px; text-align: center;
  }
  .brand-dot { display: inline-block; border-radius: 50%; background: var(--orange); vertical-align: middle; }
  .brand-name--front { left: 84px; width: 220px; top: 208px; font-size: 36px; }
  .brand-name--back { left: 0; width: 100%; top: 148px; font-size: 62px; }

  .divider {
    position: absolute; left: 392px; top: 55px; width: 8px; height: 370px;
    background: linear-gradient(to right, rgba(0,0,0,0.08), rgba(0,0,0,0));
  }

  .person { position: absolute; left: 436px; top: 114px; }
  .person__name { font-family: "Red Hat Display", sans-serif; font-weight: 700; font-size: 28px; color: var(--navy); letter-spacing: -0.2px; }
  .person__role { font-family: "Red Hat Display", sans-serif; font-size: 20px; color: var(--ink); margin-top: 0; }

  .contacts { position: absolute; left: 436px; top: 191px; list-style: none; font-family: "Roboto", sans-serif; color: var(--ink); }
  .contacts li { display: flex; align-items: center; height: 36px; font-size: 18px; }
  .contacts svg { width: 20px; height: 20px; margin-right: 22px; fill: var(--icon); flex: none; }
  .contacts .phone-icon { margin-right: 18px; }
  .contacts .phone-main { font-size: 21px; font-weight: 700; margin-right: 6px; }

  .tagline {
    position: absolute; left: 0; width: 100%; text-align: center;
    font-family: "Roboto Condensed", sans-serif; font-weight: 500; font-size: 27px; color: var(--orange); top: 286px;
  }
  .values {
    position: absolute; left: 0; width: 100%; text-align: center; top: 324px;
    font-family: "Red Hat Display", sans-serif; font-size: 20px; color: var(--navy);
  }
  .values span { margin: 0 12px; }
</style>
</head>
<body>
<main class="canvas">

  <section class="card card--front" aria-label="Business card front">
    <div class="accent-bar" style="left:0; top:150px; width:64px; height:148px;"></div>
    <div class="brand-name brand-name--front">
      <span class="brand-dot" style="width:14px;height:14px;margin-right:8px;"></span>wadol care
    </div>
    <div class="divider"></div>

    <div class="person">
      <div class="person__name">TOVAN BRELSICK</div>
      <div class="person__role">Director</div>
    </div>

    <ul class="contacts">
      <li>
        <svg class="phone-icon" viewBox="0 0 24 24" aria-hidden="true"><path d="M6.6 10.8a15.1 15.1 0 0 0 6.6 6.6l2.2-2.2a1 1 0 0 1 1-.25 11.4 11.4 0 0 0 3.6.57 1 1 0 0 1 1 1V20a1 1 0 0 1-1 1A17 17 0 0 1 3 4a1 1 0 0 1 1-1h3.5a1 1 0 0 1 1 1c0 1.25.2 2.45.57 3.57a1 1 0 0 1-.25 1z"/></svg>
        <span class="phone-main">+0427 31 64 92,</span><span>+1300 73 29 41</span>
      </li>
      <li>
        <svg viewBox="0 0 24 24" aria-hidden="true"><path d="M2 5h20v14H2z M4 7v.4l8 5.6 8-5.6V7z" fill-rule="evenodd"/></svg>
        <span>tovan@wadolire.com.au</span>
      </li>
      <li>
        <svg viewBox="0 0 24 24" aria-hidden="true"><path d="M12 2a10 10 0 1 0 0 20 10 10 0 0 0 0-20zm-1 17.9A8 8 0 0 1 4.2 10L9 14.8v1.1a2 2 0 0 0 2 2zm6.9-2.5a2 2 0 0 0-1.9-1.4h-1v-3a1 1 0 0 0-1-1H8v-2h2a1 1 0 0 0 1-1V7h2a2 2 0 0 0 2-2v-.4a8 8 0 0 1 2.9 12.8z"/></svg>
        <span>www.wadolcare.com.au</span>
      </li>
      <li>
        <svg viewBox="0 0 24 24" aria-hidden="true"><circle cx="12" cy="12" r="6"/></svg>
        <span>wadolcare.social/page</span>
      </li>
    </ul>
  </section>

  <section class="card card--back" aria-label="Business card back">
    <div class="accent-bar" style="left:0; top:150px; width:68px; height:148px;"></div>
    <div class="accent-bar" style="left:721px; top:150px; width:67px; height:148px;"></div>

    <div class="brand-name brand-name--back">
      <span class="brand-dot" style="width:22px;height:22px;margin-right:14px;"></span>wadol care
    </div>

    <div class="tagline">Aged Care Consulting Services</div>
    <div class="values">Professional<span>•</span>Reliable<span>•</span>Affordable</div>
  </section>

</main>
</body>
</html>
```